Flyer-Design für tamilisches Restaurant
Zielgruppe
Tamilisches Essen (kottu Rotti)
Aufgabenstellung
brauche eine zwei seitige A5 Flyer hoch oder quer spielt keine rolle das Hintergrund sollte Schwarz sein und paar Details in Gold wie unser Logo, das ist unsere Gedanke an design.
Auf der Vorderseite sollte, Neueröffnung am 01. März 2019 unser Hauptlogo, Facebook/ Instagram Logo in Gold mit unserer Seite (Selvo_Restaurant) und unser Motto #allaboutthebowl sein.
Auf der Rückseite, ein Bild mit kurzem Beschrieb ( Kottu Rotti das populärstes Gericht aus SriLanka)
Alle Gerichte zum mitnehmen und ab 8. März 2019 mit Lieferung.
unsere Öffnungszeiten
Montag bis Donnerstag 17.00 – 23.00 Uhr
Freitag 17.00 – 02.00 Uhr
Samstag 17.00 – 02.00 Uhr
Sonntag 17.00 – 23.00 Uhr
das Team von der Selvo freut such auf Ihren Besuch
Reservierungen unter 031 574 19 86
und noch unser Logo in klein Format

```html
<!DOCTYPE html>
<html lang="de">
<head>
<meta charset="utf-8">
<title>Selvo – Neueröffnung</title>
<link rel="stylesheet" href="https://fonts.googleapis.com/css2?family=Montserrat:wght@400;500&family=Quicksand:wght@400&family=Nothing+You+Could+Do&display=swap">
<style>
  :root {
    --ink: #050505;
    --ink-soft: #141414;
    --gold: #cfae5a;
    --white: #f4f4f4;
    --muted: #d9d9d9;
    --brand-red: #c0161d;
    --veg-red: #8e1a12;
    --veg-green: #2f5a22;
  }
  html, body { margin: 0; padding: 0; overflow: hidden; background: var(--ink); }
  .flyer {
    position: relative;
    width: 851px; height: 1200px;
    overflow: hidden;
    background: radial-gradient(ellipse at 50% 45%, var(--ink-soft) 0%, var(--ink) 75%);
    font-family: "Montserrat", sans-serif;
  }
  .produce {
    position: absolute; top: 0; bottom: 0; width: 125px;
    background: linear-gradient(180deg, var(--veg-red) 0%, var(--veg-green) 18%, #6b5a48 30%, var(--veg-red) 42%, var(--veg-green) 55%, #a0481c 63%, var(--veg-red) 72%, var(--veg-green) 82%, #6b5a48 92%, var(--veg-red) 100%);
    opacity: .85;
  }
  .produce--left { left: 0; -webkit-mask: linear-gradient(90deg, #000 60%, transparent); mask: linear-gradient(90deg, #000 60%, transparent); }
  .produce--right { right: 0; -webkit-mask: linear-gradient(270deg, #000 60%, transparent); mask: linear-gradient(270deg, #000 60%, transparent); }
  .brand-tab {
    position: absolute; left: 80px; top: 0; width: 199px; height: 164px;
    background: var(--brand-red);
    border-radius: 0 0 8px 8px;
    display: flex; align-items: center; justify-content: center; gap: 12px;
  }
  .brand-tab__dot { width: 14px; height: 14px; border-radius: 50%; background: var(--gold); }
  .brand-tab__name { font-family: "Montserrat", sans-serif; font-weight: 500; font-size: 34px; color: var(--gold); letter-spacing: 2px; }
  .sparks { position: absolute; left: 0; top: 0; }
  .headline {
    position: absolute; left: 0; right: 0; top: 285px;
    margin: 0; text-align: center;
    color: var(--white); font-weight: 400; font-size: 31px; line-height: 44px; letter-spacing: .5px;
  }
  .motto {
    position: absolute; left: 0; right: 0; top: 525px;
    margin: 0; text-align: center;
    font-family: "Nothing You Could Do", cursive; font-size: 52px; color: var(--gold); font-weight: 400;
  }
  .social {
    position: absolute; left: 150px; top: 1107px;
    display: flex; align-items: center; gap: 14px;
    font-family: "Quicksand", sans-serif; font-size: 28px; color: var(--gold);
  }
  .social__mark { width: 16px; height: 16px; border-radius: 50%; background: var(--gold); }
  .address {
    position: absolute; left: 470px; width: 280px; top: 1090px;
    margin: 0; text-align: center; font-style: normal;
    font-family: "Quicksand", sans-serif; font-size: 21px; line-height: 29px; color: var(--muted);
  }
</style>
</head>
<body>
<main class="flyer">
  <div class="produce produce--left" role="img" aria-label="Frisches Gemüse: Tomaten, Champignons, Kräuter, Karotten und Gewürze am linken Rand"></div>
  <div class="produce produce--right" role="img" aria-label="Frisches Gemüse: Tomaten, Champignons, Kräuter, Paprika und Knoblauch am rechten Rand"></div>

  <header class="brand-tab">
    <span class="brand-tab__dot"></span>
    <span class="brand-tab__name">Selvo</span>
  </header>

  <svg class="sparks" width="851" height="1200" viewBox="0 0 851 1200" aria-hidden="true">
    <g stroke="var(--white)" stroke-width="6" stroke-linecap="round" fill="none">
      <line x1="196" y1="262" x2="204" y2="276"/>
      <line x1="176" y1="300" x2="196" y2="302"/>
      <line x1="208" y1="344" x2="216" y2="334"/>
      <line x1="660" y1="284" x2="684" y2="272"/>
      <line x1="664" y1="304" x2="690" y2="300"/>
      <line x1="630" y1="344" x2="640" y2="334"/>
    </g>
  </svg>

  <h1 class="headline">NEUERÖFFNUNG AM<br>01. MÄRZ 2019!</h1>
  <p class="motto">#allaboutthebowl</p>

  <footer>
    <div class="social"><span class="social__mark"></span>Selvo_Restaurant</div>
    <address class="address">Obere Lindengasse 7<br>4563 Birkenfeld<br>tel: 031 574 19 86</address>
  </footer>
</main>
</body>
</html>
```